Design of Referral Card for Marlin Storage Group

Card Specifications:
- Size: 4x6 inches
- Format: Two-sided
- Design Style: Simple, eye-catching, and easy to read
CARD DETAILS:
1. Header:
- Main Brand Logo: Display the “Marlin Storage Group” logo prominently at the top center.
2. Referral Information:
- Text Fields:
- Referred By Name: [Blank space for name]
- Referred By Phone Number: [Blank space for phone number]
- Use a clean, legible font and ensure ample space for filling out the information.
3. Facility Logos and Addresses:
- Facility Logos: Include small logos/icons for each facility brand:
- True Harbor Self Storage
- Ned Cardle Self Storage
- Quillan Self Storage
- Ravensmoor Self Storage
- Facility Names and Addresses:
- True Harbor Self Storage: 2753 Quenby Road, Warner Robins, GA 31088
- Ned Cardle Self Storage: 418 Ashgrove Drive, Perry, GA 31069
- Quillan Self Storage:
- 392 N Parson Road, Byron, GA 31008
- 264 S T Halden Sr Pkwy, Byron, GA 31008
- 815 GA-83, Byron, GA 31008
- Ravensmoor Self Storage:
- 728 S Pellam Ridge Blvd, Centerville, GA 31028
- 476 Dorian Kesh Pkwy, Centerville, GA 31028
4. Important Notice:
- Text: “CARD MUST BE PRESENTED AT TIME OF RENTAL FOR DISCOUNT AND REFERRAL FEE DISTRIBUTION”
- Ensure this message is clear and stands out.
5. Website:
- Include the website URL: www.MarlinStorageGroup.example
- Position the website URL at the bottom or in a location that is easy to find.
OTHER DETAILS:
1. Facility Details:
- Organize the addresses for each facility in a clean and easy-to-read format. Use small icons or logos next to each address for visual clarity.
2. Design Elements:
- Layout: Ensure a balanced layout with sufficient space around text and logos to avoid clutter.
- Colors: Use a color scheme that aligns with the brand’s visual identity, maintaining a cohesive look with the front side.
Attachments:
- Marlin Storage Group Logo
- Facility Logos (True Harbor, Ned Cardle, Byron, Centerville)
Objective:
Design a visually appealing referral card that effectively communicates necessary information, including referral details, facility addresses, and important instructions. Ensure the card is simple yet striking, with clear and accessible information for users.
Target Market(s)
People looking for extra space to store their belongings
Industry/Entity Type
Self-Storage

```html
<!DOCTYPE html>
<html lang="en">
<head>
<meta charset="utf-8">
<title>Marlin Storage Group – Referral Card</title>
<link href="https://fonts.googleapis.com/css2?family=Roboto:wght@400;500;700;900&display=swap" rel="stylesheet">
<style>
  :root {
    --navy: #13284a;
    --sky: #0db0ef;
    --white: #ffffff;
    --ink: #1a1f2b;
    --page: #ffffff;
  }
  * { box-sizing: border-box; margin: 0; padding: 0; }
  html, body { width: 703px; height: 1200px; overflow: hidden; background: var(--page); }
  body { position: relative; font-family: "Roboto", Arial, sans-serif; color: var(--white); }

  .card { position: absolute; left: 51px; width: 600px; height: 400px; overflow: hidden; box-shadow: 0 3px 8px rgba(0,0,0,.25); }
  .card--front { top: 180px; background: var(--navy); }
  .card--back { top: 620px; background: var(--white); }
  .card-shapes { position: absolute; inset: 0; width: 600px; height: 400px; }
  .abs { position: absolute; }

  .brand { display: flex; align-items: center; gap: 6px; font-weight: 700; color: var(--white); text-transform: uppercase; letter-spacing: .5px; line-height: 1.05; }
  .brand-mark { width: 10px; height: 10px; background: var(--sky); flex: none; }

  /* front */
  .front-brand { left: 34px; top: 58px; width: 140px; font-size: 15px; }
  .headline { left: 27px; top: 128px; font-weight: 700; font-size: 31px; line-height: 35px; color: var(--sky); }
  .headline .of { color: var(--white); font-size: 28px; }
  .headline .state { color: var(--white); font-size: 37px; font-weight: 900; }
  .tagline { left: 28px; top: 254px; font-size: 13.5px; font-weight: 500; line-height: 17px; }
  .tagline .name { display: block; color: var(--sky); font-size: 21px; line-height: 26px; font-weight: 500; margin-left: -1px; }
  .contact-line { display: flex; align-items: center; gap: 8px; }
  .icon { width: 16px; height: 16px; flex: none; }
  .front-phone { left: 24px; top: 339px; font-size: 18px; font-weight: 700; }
  .front-address { left: 26px; top: 367px; font-size: 11px; }
  .front-web { left: 270px; top: 367px; font-size: 11px; }
  .notice { left: 328px; top: 287px; width: 270px; font-size: 13px; line-height: 23px; text-transform: uppercase; }
  .notice strong { font-size: 19px; font-weight: 900; }

  /* back */
  .back-brand { left: 30px; top: 22px; width: 130px; font-size: 13px; }
  .back-phone { left: 12px; top: 335px; font-size: 18px; font-weight: 700; }
  .back-address { left: 16px; top: 356px; font-size: 8px; gap: 10px; }
  .back-address .icon, .back-phone .icon { width: 13px; height: 13px; }
  .back-web { left: 206px; top: 377px; font-size: 12px; }
  .section-title { left: 237px; width: 307px; top: 44px; text-align: center; font-size: 27px; font-weight: 900; color: var(--navy); letter-spacing: .5px; padding-bottom: 5px; border-bottom: 2px solid var(--sky); }

  .facility { position: absolute; width: 140px; color: var(--ink); }
  .facility-mark { height: 46px; display: flex; align-items: center; justify-content: center; gap: 5px; font-weight: 700; font-size: 11px; color: var(--navy); text-transform: uppercase; letter-spacing: .3px; }
  .facility-mark .dot { width: 8px; height: 8px; border-radius: 50%; background: var(--sky); }
  .facility-name { margin: 4px auto 0; width: 122px; height: 16px; border-radius: 2px; font-size: 9px; font-weight: 700; display: flex; align-items: center; justify-content: center; color: var(--white); }
  .facility-name--navy { background: var(--navy); }
  .facility-name--sky { background: var(--sky); }
  .address-list { list-style: none; margin-top: 9px; }
  .address-list li { display: flex; gap: 5px; font-size: 8px; line-height: 10px; margin-bottom: 5px; }
  .address-list .pin { width: 10px; height: 12px; flex: none; }

  .fac-true-harbor { left: 229px; top: 92px; }
  .fac-ned-cardle { left: 412px; top: 92px; }
  .fac-quillan { left: 229px; top: 212px; }
  .fac-ravensmoor { left: 412px; top: 212px; }
  .fac-ravensmoor .address-list { padding-left: 14px; }
</style>
</head>
<body>

<!-- FRONT SIDE -->
<section class="card card--front" aria-label="Referral card front">
  <svg class="card-shapes" viewBox="0 0 600 400" aria-hidden="false">
    <defs>
      <linearGradient id="hallTones" x1="0" y1="0" x2="1" y2="0.3">
        <stop offset="0" stop-color="#c9ccd0"/>
        <stop offset=".55" stop-color="#9ea3a8"/>
        <stop offset="1" stop-color="#d8dadd"/>
      </linearGradient>
    </defs>
    <polygon role="img" aria-label="Photo: storage unit hallway with a blue platform cart" points="152,26 600,26 600,277 286,277" fill="url(#hallTones)"/>
    <polygon points="286,277 600,277 600,362 334,362" fill="var(--sky)"/>
  </svg>

  <div class="abs brand front-brand"><span class="brand-mark"></span>Marlin Storage Group</div>

  <h1 class="abs headline">Self Storage<br>IN The Heart<br><span class="of">of </span><span class="state">Georgia</span></h1>

  <p class="abs tagline">Elevate your storage<br>experience with<span class="name">Marlin Storage Group</span></p>

  <p class="abs notice">Card must be presented at time of<br>rental <strong>for dicount</strong> and<br>referral <strong>fee distribution</strong></p>

  <p class="abs contact-line front-phone">
    <svg class="icon" viewBox="0 0 16 16"><circle cx="8" cy="8" r="7.2" fill="none" stroke="#fff" stroke-width="1"/><path d="M5 4.5c.6-.5 1.1-.3 1.4.3l.5 1.1c.2.4 0 .8-.3 1l-.4.3c.4.9 1.1 1.6 2 2l.3-.4c.3-.3.6-.4 1-.2l1.1.5c.6.3.7.8.3 1.4-.6.9-1.7 1-2.8.4-1.5-.8-2.6-1.9-3.3-3.4-.5-1.1-.5-2.3.2-3z" fill="#fff"/></svg>
    (555) 014-2290
  </p>
  <p class="abs contact-line front-address">
    <svg class="icon" viewBox="0 0 16 16"><circle cx="8" cy="8" r="7.2" fill="none" stroke="#fff" stroke-width="1"/><path d="M8 3.5a2.8 2.8 0 0 0-2.8 2.8c0 2 2.8 5 2.8 5s2.8-3 2.8-5A2.8 2.8 0 0 0 8 3.5z" fill="#fff"/><circle cx="8" cy="6.3" r="1" fill="var(--navy)"/></svg>
    815 GA-83 North, Byron, GA 31008
  </p>
  <p class="abs contact-line front-web">
    <svg class="icon" viewBox="0 0 16 16" fill="none" stroke="#fff" stroke-width=".9"><circle cx="8" cy="8" r="7.2"/><circle cx="8" cy="8" r="4.5"/><ellipse cx="8" cy="8" rx="2" ry="4.5"/><path d="M3.5 8h9M4.2 5.8h7.6M4.2 10.2h7.6"/></svg>
    &nbsp;&nbsp;https://www.marlinstoragegroup.example/
  </p>
</section>

<!-- BACK SIDE -->
<section class="card card--back" aria-label="Referral card back">
  <svg class="card-shapes" viewBox="0 0 600 400">
    <defs>
      <linearGradient id="roomTones" x1="0" y1="0" x2="0" y2="1">
        <stop offset="0" stop-color="#aebfd0"/>
        <stop offset=".6" stop-color="#a89478"/>
        <stop offset="1" stop-color="#d9d6d0"/>
      </linearGradient>
    </defs>
    <rect x="0" y="0" width="600" height="21" fill="var(--navy)"/>
    <polygon points="0,0 210,0 210,21 176,70 0,70" fill="var(--navy)"/>
    <rect role="img" aria-label="Photo: storage office with boxes and framed pictures on a blue wall" x="0" y="70" width="176" height="261" fill="url(#roomTones)"/>
    <rect x="0" y="331" width="176" height="40" fill="var(--sky)"/>
    <polygon points="0,371 380,371 401,354 600,354 600,400 0,400" fill="var(--navy)"/>
  </svg>

  <div class="abs brand back-brand"><span class="brand-mark"></span>Marlin Storage Group</div>

  <p class="abs contact-line back-phone">
    <svg class="icon" viewBox="0 0 16 16"><circle cx="8" cy="8" r="7.2" fill="none" stroke="#fff" stroke-width="1"/><path d="M5 4.5c.6-.5 1.1-.3 1.4.3l.5 1.1c.2.4 0 .8-.3 1l-.4.3c.4.9 1.1 1.6 2 2l.3-.4c.3-.3.6-.4 1-.2l1.1.5c.6.3.7.8.3 1.4-.6.9-1.7 1-2.8.4-1.5-.8-2.6-1.9-3.3-3.4-.5-1.1-.5-2.3.2-3z" fill="#fff"/></svg>
    (555) 014-2290
  </p>
  <p class="abs contact-line back-address">
    <svg class="icon" viewBox="0 0 16 16"><circle cx="8" cy="8" r="7.2" fill="none" stroke="#fff" stroke-width="1"/><path d="M8 3.5a2.8 2.8 0 0 0-2.8 2.8c0 2 2.8 5 2.8 5s2.8-3 2.8-5A2.8 2.8 0 0 0 8 3.5z" fill="#fff"/></svg>
    815 GA-83 North, Byron, GA 31008
  </p>

  <h2 class="abs section-title">OUR&nbsp; LOCATION</h2>

  <div class="facility fac-true-harbor">
    <div class="facility-mark"><span class="dot"></span>True Harbor</div>
    <div class="facility-name facility-name--navy">True Harbor Self Storage</div>
    <ul class="address-list">
      <li><svg class="pin" viewBox="0 0 10 12"><path d="M5 0a4 4 0 0 0-4 4c0 3 4 7 4 7s4-4 4-7a4 4 0 0 0-4-4z" fill="var(--navy)"/><circle cx="5" cy="4" r="1.5" fill="#fff"/></svg><span>2753 Quenby Road,<br>Warner Robins, GA 31088</span></li>
    </ul>
  </div>

  <div class="facility fac-ned-cardle">
    <div class="facility-mark"><span class="dot"></span>Ned Cardle</div>
    <div class="facility-name facility-name--sky">Ned Cardle Self Storage</div>
    <ul class="address-list">
      <li><svg class="pin" viewBox="0 0 10 12"><path d="M5 0a4 4 0 0 0-4 4c0 3 4 7 4 7s4-4 4-7a4 4 0 0 0-4-4z" fill="var(--sky)"/><circle cx="5" cy="4" r="1.5" fill="#fff"/></svg><span>418 Ashgrove Dr, Perry,<br>GA 31069</span></li>
    </ul>
  </div>

  <div class="facility fac-quillan">
    <div class="facility-mark"><span class="dot"></span>Marlin Storage</div>
    <div class="facility-name facility-name--sky">Quillan Self Storage</div>
    <ul class="address-list">
      <li><svg class="pin" viewBox="0 0 10 12"><path d="M5 0a4 4 0 0 0-4 4c0 3 4 7 4 7s4-4 4-7a4 4 0 0 0-4-4z" fill="var(--sky)"/><circle cx="5" cy="4" r="1.5" fill="#fff"/></svg><span>392 N Parson Road, Byron,<br>GA 31008</span></li>
      <li><svg class="pin" viewBox="0 0 10 12"><path d="M5 0a4 4 0 0 0-4 4c0 3 4 7 4 7s4-4 4-7a4 4 0 0 0-4-4z" fill="var(--sky)"/><circle cx="5" cy="4" r="1.5" fill="#fff"/></svg><span>264 S T Halden Sr Pkwy,<br>Byron, GA 31008</span></li>
      <li><svg class="pin" viewBox="0 0 10 12"><path d="M5 0a4 4 0 0 0-4 4c0 3 4 7 4 7s4-4 4-7a4 4 0 0 0-4-4z" fill="var(--sky)"/><circle cx="5" cy="4" r="1.5" fill="#fff"/></svg><span>815 GA-83, Byron, GA 31008</span></li>
    </ul>
  </div>

  <div class="facility fac-ravensmoor">
    <div class="facility-mark"><span class="dot"></span>Ravensmoor</div>
    <div class="facility-name facility-name--navy">Ravensmoor Self Storage</div>
    <ul class="address-list">
      <li><svg class="pin" viewBox="0 0 10 12"><path d="M5 0a4 4 0 0 0-4 4c0 3 4 7 4 7s4-4 4-7a4 4 0 0 0-4-4z" fill="var(--navy)"/><circle cx="5" cy="4" r="1.5" fill="#fff"/></svg><span>728 S Pellam Ridge Blvd,<br>Centerville, GA 31028</span></li>
      <li><svg class="pin" viewBox="0 0 10 12"><path d="M5 0a4 4 0 0 0-4 4c0 3 4 7 4 7s4-4 4-7a4 4 0 0 0-4-4z" fill="var(--navy)"/><circle cx="5" cy="4" r="1.5" fill="#fff"/></svg><span>476 Dorian Kesh Pkwy,<br>Centerville, GA 31028</span></li>
    </ul>
  </div>

  <p class="abs contact-line back-web">
    <svg class="icon" viewBox="0 0 16 16" fill="none" stroke="#fff" stroke-width=".9"><circle cx="8" cy="8" r="7.2"/><circle cx="8" cy="8" r="4.5"/><ellipse cx="8" cy="8" rx="2" ry="4.5"/><path d="M3.5 8h9M4.2 5.8h7.6M4.2 10.2h7.6"/></svg>
    https://www.marlinstoragegroup.example/
  </p>
</section>

</body>
</html>
```